Trovan Dirtworks LLC - Excavation Contractor in Idaho

Wordpress website, visually appealing....Company is Veteran owned business, owner SGT Harold Mensick USMC, anything from laser grading to cleaning up your property we do various Skidsteer work and are always buying new attachments to do more jobs. Services include: excavation, grading, snow plowing, demolition and cleanup, fence post hole drilling, trenching.

Target Market(s)

Contractors and Home owners needing projects completed

Industry/Entity Type

Construction

Number of Pages Required

3 page

Font styles to use
Sans Serif

Requirements
Must have
• Site visually appealing and easy to navigate.
Nice to have
• Maybe bold colors?

```html
<!DOCTYPE html>
<html lang="en">
<head>
<meta charset="utf-8">
<title>Trovan Dirtworks LLC – Excavation Contractor in Idaho</title>
<link rel="stylesheet" href="https://fonts.googleapis.com/css2?family=Bebas+Neue&family=Roboto:wght@400;500;700&display=swap">
<style>
:root{
  --red:#e01f2d;
  --red-dark:#b8141f;
  --ink:#1c1c1c;
  --panel:#262626;
  --deep:#161616;
  --text:#555;
  --muted:#999;
  --white:#fff;
  --line:#e4e4e4;
}
*{box-sizing:border-box;margin:0;padding:0}
html,body{width:1200px;height:4756px;overflow:hidden}
body{font-family:'Roboto',Arial,sans-serif;color:var(--text);background:var(--white);font-size:13px;line-height:1.6}
.display{font-family:'Bebas Neue','Oswald',sans-serif;font-weight:400;letter-spacing:.5px}
section,header,footer{position:relative;width:1200px;overflow:hidden}
.btn{display:inline-block;font-family:'Roboto',sans-serif;font-weight:700;font-size:12px;text-transform:uppercase;letter-spacing:.5px;color:var(--white);border-radius:22px;padding:0 34px;height:38px;line-height:38px}
.btn-red{background:var(--red);box-shadow:0 4px 10px rgba(0,0,0,.25)}
.btn-black{background:var(--ink);height:32px;line-height:32px;padding:0 26px;font-size:11px}
.section-title{font-size:46px;color:var(--red);text-align:center;line-height:1}
.section-title::after{content:"";display:block;width:70px;height:3px;background:var(--red);margin:10px auto 0}

/* hero */
.hero{height:740px}
.hero-bg{position:absolute;inset:0;clip-path:polygon(0 0,100% 0,100% 100%,0 90%);
  background:linear-gradient(180deg,#7d8d72 0%,#8e7f62 30%,#6e5a44 60%,#4c3b2c 100%)}
.hero-shade{position:absolute;inset:0;clip-path:polygon(0 0,100% 0,100% 100%,0 90%);background:linear-gradient(90deg,rgba(0,0,0,.45),rgba(0,0,0,0) 70%)}
.nav{position:absolute;top:0;left:0;right:0;height:56px;background:rgba(0,0,0,.55);display:flex;align-items:center;padding:0 112px}
.brand{font-family:'Bebas Neue',sans-serif;font-size:26px;color:var(--white);display:flex;align-items:center;gap:8px;letter-spacing:1px}
.brand-dot{width:14px;height:14px;background:var(--red);display:inline-block}
.menu{display:flex;gap:26px;margin-left:auto;margin-right:120px}
.menu a{color:var(--white);font-size:13px;font-weight:500}
.menu a.active{color:var(--red)}
.login{background:var(--red);color:var(--white);font-size:12px;font-weight:700;padding:0 26px;height:28px;line-height:28px;border-radius:3px}
.nav-social{display:flex;gap:8px;margin-left:18px}
.nav-social span{width:10px;height:10px;border-radius:50%;background:var(--white);opacity:.85}
.hero-copy{position:absolute;left:112px;top:240px;width:520px;color:var(--white)}
.hero-copy h1{font-size:118px;line-height:.95;color:var(--white);margin-bottom:26px;width:900px}
.hero-copy p{font-size:14px;line-height:1.55;margin-bottom:30px}

/* about */
.about{height:460px;text-align:center;padding-top:60px}
.about p{width:840px;margin:34px auto 0;font-size:13px;color:var(--text)}
.about p + p{margin-top:16px}
.about .btn{margin-top:40px}

/* services */
.services-head{height:100px;padding-top:20px}
.service-row{height:380px;display:flex}
.service-text{width:600px;padding:0 112px;display:flex;flex-direction:column;justify-content:center;color:var(--white)}
.service-text h3{font-size:32px;line-height:1;margin-bottom:16px}
.service-text p{font-size:13px;line-height:1.6;margin-bottom:24px;width:390px}
.service-text .btn{align-self:flex-start}
.red{background:var(--red)}
.dark{background:var(--panel)}
.service-row .dark{padding-left:50px}
.photo{width:600px;height:100%}
.ph-excavation{background:linear-gradient(180deg,#b9c9d6 0%,#8f9a80 45%,#4b4a3c 100%)}
.ph-grading{background:linear-gradient(180deg,#aec6dc 0%,#c9b79a 40%,#5c7a3a 65%,#3f5228 100%)}
.ph-snow{background:linear-gradient(180deg,#c7cfd4 0%,#8d9294 50%,#5a5e5c 100%)}
.ph-demolition{background:linear-gradient(180deg,#d3d7da 0%,#7a8f9c 35%,#3d5e78 60%,#6b5a3e 100%)}
.view-more{position:absolute;left:50%;top:2808px;transform:translateX(-50%)}

/* blog */
.blog{height:680px;padding:120px 112px 0}
.blog-head{display:flex;align-items:center;justify-content:space-between}
.blog-head h2{font-size:46px;color:var(--red);line-height:1}
.see-all{border:1px solid #ccc;font-size:11px;font-weight:700;color:var(--ink);padding:0 12px;height:28px;line-height:28px;width:110px;display:flex;justify-content:space-between}
.cards{display:flex;gap:32px;margin-top:34px}
.card{width:312px;height:432px;background:var(--white);box-shadow:0 2px 14px rgba(0,0,0,.18);position:relative}
.card-photo{height:190px;position:relative}
.cp-1{background:linear-gradient(180deg,#9fb0bf 0%,#6f7564 55%,#3f3a30 100%)}
.cp-2{background:linear-gradient(180deg,#e5e7ea 0%,#a9a9a4 55%,#4d4a42 100%)}
.cp-3{background:linear-gradient(180deg,#b8c6d2 0%,#4c6784 50%,#7a6445 100%)}
.card-date{position:absolute;left:0;bottom:-12px;background:var(--red);color:var(--white);font-size:11px;padding:0 16px;height:24px;line-height:24px}
.card-body{padding:30px 20px 0}
.card-body h4{font-size:16px;font-weight:700;color:var(--ink);line-height:1.35;margin-bottom:12px}
.card-body p{font-size:12px;color:var(--text);line-height:1.55}
.card-plus{position:absolute;right:14px;bottom:14px;width:32px;height:32px;background:var(--ink)}

/* stats */
.stats{height:440px}
.stats-bg{position:absolute;inset:0;clip-path:polygon(0 0,100% 0,100% 82%,0 100%);background:linear-gradient(180deg,#1e1e1e,#111 60%,#1b1b1b)}
.stat-list{position:absolute;top:130px;left:200px;display:flex;gap:56px}
.stat{width:160px;text-align:center;color:var(--white)}
.stat-ring{width:120px;height:120px;border-radius:50%;border:3px solid var(--red);margin:0 auto 20px;display:flex;align-items:center;justify-content:center;font-size:46px;font-family:'Bebas Neue',sans-serif}
.stat p{font-size:12px;font-weight:500}

/* testimonials */
.testimonials{height:360px;padding-top:60px;text-align:center}
.testimonials blockquote{width:860px;margin:34px auto 0;font-size:13px;font-style:italic;line-height:1.6;color:var(--text)}
.t-name{color:var(--red);font-weight:700;font-size:14px;margin-top:20px}
.t-role{font-size:11px;color:var(--muted)}
.arrow{position:absolute;top:200px;width:36px;height:36px;border:1px solid #ccc;display:flex;align-items:center;justify-content:center}
.arrow.prev{left:60px}.arrow.next{right:60px}

/* footer */
.site-footer{height:456px;background:var(--ink);color:#cfcfcf;padding:70px 112px 0}
.f-cols{display:flex}
.f-col h5{font-family:'Roboto',sans-serif;font-size:14px;font-weight:700;color:var(--white);text-transform:uppercase;margin-bottom:6px}
.f-col h5::after{content:"";display:block;width:34px;height:2px;background:var(--red);margin-top:6px;margin-bottom:12px}
.f-col li{list-style:none;font-size:12px;line-height:2}
.f-col p{font-size:12px;line-height:1.6}
.f-col .label{color:var(--white);font-weight:500;margin-top:8px}
.f-links{width:190px}.f-services{width:220px}.f-contact{width:280px}.f-news{width:310px}
.newsletter{margin-top:20px;width:270px;height:34px;background:var(--white);border-radius:18px;position:relative;padding-left:14px;font-size:11px;color:var(--muted);line-height:34px}
.newsletter span{position:absolute;right:3px;top:3px;width:28px;height:28px;border-radius:50%;background:var(--red)}
.f-social{display:flex;gap:10px;margin-top:22px}
.f-social span{width:34px;height:34px;border-radius:50%;border:1px solid #777}
.f-bottom{position:absolute;left:0;right:0;bottom:0;height:60px;border-top:1px solid #3a3a3a;display:flex;align-items:center;justify-content:space-between;padding:0 112px;font-size:12px}
</style>
</head>
<body>

<header class="hero">
  <div class="hero-bg" role="img" aria-label="Compact excavator digging a graded dirt site"></div>
  <div class="hero-shade"></div>
  <nav class="nav">
    <div class="brand"><span class="brand-dot"></span>Trovan Dirtworks LLC</div>
    <div class="menu"><a class="active">Home</a><a>About Us</a><a>Services</a><a>Blog</a><a>Contact</a></div>
    <a class="login">Login</a>
    <div class="nav-social"><span></span><span></span></div>
  </nav>
  <div class="hero-copy">
    <h1 class="display">Trovan Dirtworks LLC</h1>
    <p>Lorem ipsum dolor sit amet, consectetur adipiscing elit, sed do eiusmod tempor incididunt ut labore et dolore magna aliqua. Ut enim ad minim veniam, quis nostrud exercitation ullamco laboris nisi.</p>
    <a class="btn btn-red">Get Started</a>
  </div>
</header>

<section class="about">
  <h2 class="section-title display">About Trovan Dirtworks LLC</h2>
  <p>Lorem ipsum dolor sit amet, consectetur adipiscing elit, sed do eiusmod tempor incididunt ut labore et dolore magna aliqua. Ut enim ad minim veniam, quis nostrud exercitation ullamco laboris nisi ut aliquip ex ea commodo consequat. Duis aute irure dolor in reprehenderit in voluptate velit esse cillum dolore.</p>
  <p>Lorem ipsum dolor sit amet, consectetur adipiscing elit, sed do eiusmod tempor incididunt ut labore et dolore magna aliqua. Ut enim ad minim veniam, quis nostrud exercitation ullamco laboris nisi ut aliquip ex ea commodo consequat. Duis aute irure dolor in reprehenderit in voluptate velit esse cillum dolore.</p>
  <a class="btn btn-red">Read More</a>
</section>

<section class="services-head">
  <h2 class="section-title display">Our Services</h2>
</section>

<section class="service-row">
  <div class="service-text red">
    <h3 class="display">Excavation</h3>
    <p>Lorem ipsum dolor sit amet, consectetur adipiscing elit, sed do eiusmod tempor incididunt ut labore et dolore magna aliqua. Ut enim ad minim veniam, quis nostrud exercitation ullamco laboris nisi ut aliquip ex ea commodo consequat. Duis aute irure dolor in.</p>
    <a class="btn btn-black">Read More</a>
  </div>
  <div class="photo ph-excavation" role="img" aria-label="Tracked skid steer parked on a muddy field"></div>
</section>
<section class="service-row">
  <div class="photo ph-grading" role="img" aria-label="Freshly graded lawn area at sunset"></div>
  <div class="service-text dark">
    <h3 class="display">Grading</h3>
    <p>Lorem ipsum dolor sit amet, consectetur adipiscing elit, sed do eiusmod tempor incididunt ut labore et dolore magna aliqua. Ut enim ad minim veniam, quis nostrud exercitation ullamco laboris nisi ut aliquip ex ea commodo consequat. Duis aute irure dolor in.</p>
    <a class="btn btn-black">Read More</a>
  </div>
</section>
<section class="service-row">
  <div class="service-text red">
    <h3 class="display">Snow Plowing</h3>
    <p>Lorem ipsum dolor sit amet, consectetur adipiscing elit, sed do eiusmod tempor incididunt ut labore et dolore magna aliqua. Ut enim ad minim veniam, quis nostrud exercitation ullamco laboris nisi ut aliquip ex ea commodo consequat. Duis aute irure dolor in.</p>
    <a class="btn btn-black">Read More</a>
  </div>
  <div class="photo ph-snow" role="img" aria-label="Compact track loader with bucket on a gravel yard"></div>
</section>
<section class="service-row">
  <div class="photo ph-demolition" role="img" aria-label="Skid steer loading debris into a roll-off dumpster"></div>
  <div class="service-text dark">
    <h3 class="display">Demolition and Cleanup</h3>
    <p>Lorem ipsum dolor sit amet, consectetur adipiscing elit, sed do eiusmod tempor incididunt ut labore et dolore magna aliqua. Ut enim ad minim veniam, quis nostrud exercitation ullamco laboris nisi ut aliquip ex ea commodo consequat. Duis aute irure dolor in.</p>
    <a class="btn btn-black">Read More</a>
  </div>
</section>

<section class="blog">
  <div class="blog-head">
    <h2 class="display">From Our Blog</h2>
    <div class="see-all">SEE ALL <svg width="10" height="28" viewBox="0 0 10 28"><path d="M2 12l3 4 3-4z" fill="#1c1c1c"/></svg></div>
  </div>
  <div class="cards">
    <article class="card">
      <div class="card-photo cp-1" role="img" aria-label="Skid steer working on a job site"><span class="card-date">25.03.2021 &nbsp;By : Admin</span></div>
      <div class="card-body">
        <h4>Lorem ipsum dolor sit amet, consectetur adipiscing elit, sed do eiusmod</h4>
        <p>Lorem ipsum dolor sit amet, consectetur adipiscing elit, sed do eiusmod tempor incididunt ut labore.</p>
      </div>
      <span class="card-plus"><svg width="32" height="32" viewBox="0 0 32 32"><path d="M16 10v12M10 16h12" stroke="#fff" stroke-width="2.5"/></svg></span>
    </article>
    <article class="card">
      <div class="card-photo cp-2" role="img" aria-label="Compact loader with attachment in a yard"><span class="card-date">25.03.2021 &nbsp;By : Admin</span></div>
      <div class="card-body">
        <h4>Lorem ipsum dolor sit amet, consectetur adipiscing elit, sed do eiusmod</h4>
        <p>Lorem ipsum dolor sit amet, consectetur adipiscing elit, sed do eiusmod tempor incididunt ut labore.</p>
      </div>
      <span class="card-plus"><svg width="32" height="32" viewBox="0 0 32 32"><path d="M16 10v12M10 16h12" stroke="#fff" stroke-width="2.5"/></svg></span>
    </article>
    <article class="card">
      <div class="card-photo cp-3" role="img" aria-label="Loader beside a blue dumpster full of debris"><span class="card-date">25.03.2021 &nbsp;By : Admin</span></div>
      <div class="card-body">
        <h4>Lorem ipsum dolor sit amet, consectetur adipiscing elit, sed do eiusmod</h4>
        <p>Lorem ipsum dolor sit amet, consectetur adipiscing elit, sed do eiusmod tempor incididunt ut labore.</p>
      </div>
      <span class="card-plus"><svg width="32" height="32" viewBox="0 0 32 32"><path d="M16 10v12M10 16h12" stroke="#fff" stroke-width="2.5"/></svg></span>
    </article>
  </div>
</section>

<a class="btn btn-red view-more">View More</a>

<section class="stats">
  <div class="stats-bg" role="img" aria-label="Dark textured background"></div>
  <div class="stat-list">
    <div class="stat"><div class="stat-ring">150</div><p>Lorem ipsum dolor sit amet</p></div>
    <div class="stat"><div class="stat-ring">181</div><p>Lorem ipsum dolor sit amet</p></div>
    <div class="stat"><div class="stat-ring">202</div><p>Lorem ipsum dolor sit amet</p></div>
    <div class="stat"><div class="stat-ring">312</div><p>Lorem ipsum dolor sit amet</p></div>
  </div>
</section>

<section class="testimonials">
  <h2 class="section-title display">Testimonials</h2>
  <blockquote>Lorem ipsum dolor sit amet, consectetur adipiscing elit, sed do eiusmod tempor incididunt ut labore et dolore magna aliqua. Ut enim ad minim veniam, quis nostrud exercitation ullamco laboris nisi ut aliquip ex ea commodo consequat. Duis aute irure dolor in reprehenderit in voluptate velit esse cillum dolore eu fugiat nulla pariatur. Excepteur sint occaecat cupidatat non proident, sunt in culpa qui officia deserunt mollit anim.</blockquote>
  <p class="t-name">Dana Whitfield</p>
  <p class="t-role">Lorem Ipsum</p>
  <span class="arrow prev"><svg width="12" height="12" viewBox="0 0 12 12"><path d="M8 1L3 6l5 5" fill="none" stroke="#555" stroke-width="1.6"/></svg></span>
  <span class="arrow next"><svg width="12" height="12" viewBox="0 0 12 12"><path d="M4 1l5 5-5 5" fill="none" stroke="#555" stroke-width="1.6"/></svg></span>
</section>

<footer class="site-footer">
  <div class="f-cols">
    <div class="f-col f-links">
      <h5>Quick Links</h5>
      <ul><li>Home</li><li>About</li><li>Services</li><li>Blog</li><li>Contact</li></ul>
    </div>
    <div class="f-col f-services">
      <h5>Services</h5>
      <ul><li>Excavation</li><li>Grading</li><li>Snow Plowing</li><li>Demolition And Cleanup</li><li>Fence Post Hole Drilling</li><li>Trenching</li></ul>
    </div>
    <div class="f-col f-contact">
      <h5>Contact Us</h5>
      <p class="label">ADDRESS</p>
      <p>Lorem ipsum dolor sit amet,<br>consectetur adipiscing</p>
      <p class="label">PHONE</p>
      <p>&#9742; 208-555-0147</p>
      <p class="label">EMAIL</p>
      <p>info@trovandirtworks.com</p>
    </div>
    <div class="f-col f-news">
      <h5>Newsletter</h5>
      <p>Lorem ipsum dolor sit amet, consectetur adipiscing elit, sed do eiusmod tempor.</p>
      <div class="newsletter">Enter Email<span></span></div>
      <div class="f-social"><span></span><span></span><span></span></div>
    </div>
  </div>
  <div class="f-bottom">
    <span>© 2021 Trovan Dirtworks LLC All Rights Reserved</span>
    <span>Terms of use | Privacy Policy</span>
  </div>
</footer>

</body>
</html>
```